we are an outdoor outlet in a country club that has a variety of outlets. The Club is called Lanterns and is located in Cairo, Egypt. This garden menu will include cuisines from the Mediterranean, Asia and Texmex. we need a menu that is colorful and would fit an A3 size, back and front are to be used. Attached is the old menu currently in use (Garden Menu 2012.pdf is just for reference) and the new menu text for you to use is under the name Garden Menu Fall 2013
thank you.

```html
<!DOCTYPE html>
<html lang="en">
<head>
<meta charset="utf-8">
<title>Lanterns Garden Menu</title>
<link href="https://fonts.googleapis.com/css2?family=Cabin:wght@400;500;600;700&display=swap" rel="stylesheet">
<style>
:root{
  --paper-light:#f3cd8c;
  --paper-dark:#e6b36a;
  --purple:#9a2585;
  --orange:#e4561e;
  --ink:#2e2418;
  --ink-soft:#4a3a28;
  --leaf:#8cc63f;
  --leaf-dark:#6aa82a;
  --frame:#d9541f;
  --divider:#8e2a82;
}
*{box-sizing:border-box;margin:0;padding:0}
html,body{width:1200px;height:845px;overflow:hidden;background:#fff}
body{font-family:"Cabin",Arial,sans-serif;color:var(--ink)}
.spread{position:relative;width:1200px;height:845px}
.page{position:absolute;top:0;height:845px;width:598px;overflow:hidden;
  background:radial-gradient(ellipse at 40% 40%,var(--paper-light) 0%,var(--paper-dark) 100%)}
.page--front{left:0}
.page--back{left:602px}
.divider{position:absolute;left:598px;top:0;width:4px;height:845px;background:var(--divider)}
.grass{position:absolute;background:linear-gradient(180deg,var(--leaf) 0%,var(--leaf-dark) 100%)}
.grass--top{border-radius:0 0 40% 40%/0 0 100% 100%}
.grass--bottom{border-radius:50% 50% 0 0/100% 100% 0 0}
.brand-name{position:absolute;font-size:30px;font-weight:700;color:var(--ink);text-align:center;line-height:1;width:220px;letter-spacing:.5px}
.web{position:absolute;font-size:9px;font-weight:700;color:var(--ink);text-align:center;width:220px}
.corner-title{position:absolute;font-size:21px;font-weight:700;color:var(--purple);line-height:1}
.section-head{position:absolute;font-size:12px;font-weight:600;color:var(--orange);text-align:center;line-height:1}
.item{position:absolute;width:250px}
.item__row{display:flex;justify-content:space-between;font-size:10.5px;line-height:1.1;color:var(--ink)}
.item__price{font-size:10px;width:40px;white-space:nowrap}
.item__desc{font-size:5.8px;line-height:1.25;color:var(--ink-soft);width:170px;margin-top:1px}
.note{position:absolute;font-size:6px;line-height:1.3;color:var(--ink-soft);width:230px}
.photo{position:absolute;border:4px solid var(--frame);box-shadow:1px 2px 3px rgba(0,0,0,.3)}
.contact{position:absolute;font-size:15px;font-weight:700;color:var(--ink)}
.contact em{font-style:normal;color:var(--purple)}
</style>
</head>
<body>
<div class="spread">

<section class="page page--front">
  <div class="grass grass--top" style="left:235px;top:0;width:200px;height:28px" role="img" aria-label="green grass border"></div>
  <div class="grass grass--bottom" style="left:0;top:800px;width:598px;height:45px" role="img" aria-label="green grass border"></div>

  <div class="brand-name" style="left:39px;top:100px">Lanterns</div>
  <div class="web" style="left:39px;top:139px">www.lanternsclubcairo.com</div>

  <h1 class="corner-title" style="left:37px;top:164px">Mediterranean Corner</h1>

  <h2 class="section-head" style="left:25px;top:204px;width:250px">~Pizza &amp; Pasta~</h2>
  <div class="item" style="left:25px;top:227px">
    <div class="item__row"><span>Pizza Margarita</span><span class="item__price">L.E X.xx</span></div>
    <p class="item__desc">(Choose your toppings) Create your own pasta</p>
  </div>
  <p class="note" style="left:25px;top:251px">Type: Spaghetti, Tagliatelle, Penne</p>
  <p class="note" style="left:25px;top:266px">Sauces: Napolitana, Bolognese, Alfredo</p>
  <p class="note" style="left:25px;top:281px">Toppings: Bell peppers, olives, tomato, onion Mushroom, chicken, tuna, pepperoni Smoked salmon, shrimps Lasagna</p>

  <h2 class="section-head" style="left:25px;top:315px;width:250px">~Sandwiches~</h2>
  <p class="note" style="left:25px;top:330px;width:250px;text-align:center">(Served with French fries or a garden salad)</p>
  <div class="item" style="left:25px;top:346px"><div class="item__row"><span>Beef or chicken shawerma</span><span class="item__price">L.E X.xx</span></div></div>
  <div class="item" style="left:25px;top:366px"><div class="item__row"><span>Grilled kofta</span><span class="item__price">L.E X.xx</span></div></div>
  <div class="item" style="left:25px;top:387px">
    <div class="item__row"><span>Greek lamb gyro</span><span class="item__price">L.E X.xx</span></div>
    <p class="item__desc">in pita bread with Tzatziki</p>
  </div>
  <div class="item" style="left:25px;top:414px">
    <div class="item__row"><span>Club sandwich</span><span class="item__price">L.E X.xx</span></div>
    <p class="item__desc">with smoked beef, turkey, egg</p>
  </div>

  <h2 class="section-head" style="left:25px;top:455px;width:250px">~Main Courses~</h2>
  <div class="item" style="left:25px;top:478px">
    <div class="item__row"><span>Veal parmeggiana</span><span class="item__price">L.E X.xx</span></div>
    <p class="item__desc">Breaded veal escalope topped with melted cheese and tomato sauce served with Spaghetti</p>
  </div>
  <div class="item" style="left:25px;top:513px">
    <div class="item__row"><span>Chicken a la francaise</span><span class="item__price">L.E X.xx</span></div>
    <p class="item__desc">Pan fried chicken breast in a mushroom cream sauce with vegetables white rice</p>
  </div>
  <div class="item" style="left:25px;top:547px">
    <div class="item__row"><span>Grilled salmon</span><span class="item__price">L.E X.xx</span></div>
    <p class="item__desc">Salmon steak charcoal grilled with avocado tomato relish and creamy mushroom risotto</p>
  </div>
  <div class="item" style="left:25px;top:582px">
    <div class="item__row"><span>Moroccan chicken</span><span class="item__price">L.E X.xx</span></div>
    <p class="item__desc">Chicken cubes simmered with spices and olives served with tomato rice</p>
  </div>
  <div class="item" style="left:25px;top:615px">
    <div class="item__row"><span>Filet</span><span class="item__price">L.E X.xx</span></div>
    <p class="item__desc">Tender filet grilled to your liking served with mashed potato and creamed spinach</p>
  </div>
  <p class="note" style="left:25px;top:650px">Choice of sauces: Brown mushroom, Green Peppercorn, Gorgonzola</p>

  <div class="photo" style="left:24px;top:702px;width:74px;height:68px;transform:rotate(-4deg);background:linear-gradient(135deg,#f4f1ec,#8a5a3c)" role="img" aria-label="Photo of plated desserts"></div>
  <div class="photo" style="left:146px;top:712px;width:120px;height:86px;transform:rotate(-8deg);background:linear-gradient(135deg,#c96b4a,#6f8b3e)" role="img" aria-label="Photo of sliced smoked meat with salad"></div>
  <div class="photo" style="left:384px;top:734px;width:90px;height:74px;transform:rotate(-3deg);background:linear-gradient(135deg,#f5f3f0,#b8453a)" role="img" aria-label="Photo of canapés on white plates"></div>

  <h2 class="section-head" style="left:324px;top:39px;width:250px">~Soup~</h2>
  <div class="item" style="left:324px;top:61px">
    <div class="item__row"><span>Tomato basil</span><span class="item__price">L.E X.xx</span></div>
    <p class="item__desc" style="width:210px">Simmered tomato soup finished with fresh basil and cream</p>
  </div>
  <div class="item" style="left:324px;top:88px">
    <div class="item__row"><span>Chicken cream</span><span class="item__price">L.E X.xx</span></div>
    <p class="item__desc" style="width:210px">Chicken broth with roasted chicken cubes, pine nuts, and cream</p>
  </div>
  <div class="item" style="left:324px;top:115px">
    <div class="item__row"><span>Moroccan harira</span><span class="item__price">L.E X.xx</span></div>
    <p class="item__desc">Vegetable broth with fresh tomato, chickpeas, lentil, cilantro and diced lamb</p>
  </div>

  <h2 class="section-head" style="left:324px;top:160px;width:250px">~Appetizers~</h2>
  <div class="item" style="left:324px;top:182px"><div class="item__row"><span>Salmon tartare</span><span class="item__price">L.E X.xx</span></div><p class="item__desc" style="width:200px">seasoned with lemon juice, garlic, and crushed black pepper</p></div>
  <div class="item" style="left:324px;top:209px"><div class="item__row"><span>Roasted eggplant rolls</span><span class="item__price">L.E X.xx</span></div><p class="item__desc">with herbed ricotta cheese and pine nuts</p></div>
  <div class="item" style="left:324px;top:237px"><div class="item__row"><span>Falafel in mini pita</span><span class="item__price">L.E X.xx</span></div><p class="item__desc">served with tehina and oriental salsa</p></div>
  <div class="item" style="left:324px;top:264px"><div class="item__row"><span>Mankousha</span><span class="item__price">L.E X.xx</span></div><p class="item__desc">with thyme and olive oil</p></div>
  <div class="item" style="left:324px;top:292px"><div class="item__row"><span>Fried kobeba</span><span class="item__price">L.E X.xx</span></div><p class="item__desc">with minced meat, spices, and pine nuts</p></div>
  <div class="item" style="left:324px;top:319px"><div class="item__row"><span>Fried calamari a la Romana</span><span class="item__price">L.E X.xx</span></div><p class="item__desc">served with aioli</p></div>
  <div class="item" style="left:324px;top:347px"><div class="item__row"><span>Samboussek</span><span class="item__price">L.E X.xx</span></div><p class="item__desc">with herbed white cheese and mint</p></div>
  <div class="item" style="left:324px;top:374px"><div class="item__row"><span>Oriental sausage</span><span class="item__price">L.E X.xx</span></div><p class="item__desc">sautéed with garlic and onion</p></div>
  <div class="item" style="left:324px;top:402px"><div class="item__row"><span>Mini vine</span><span class="item__price">L.E X.xx</span></div><p class="item__desc">leaves with a yoghurt dip</p></div>
  <div class="item" style="left:324px;top:429px"><div class="item__row"><span>Fatouch</span><span class="item__price">L.E X.xx</span></div><p class="item__desc">with a pomegranate syrup dressing</p></div>
  <div class="item" style="left:324px;top:457px"><div class="item__row"><span>Hummus</span><span class="item__price">L.E X.xx</span></div><p class="item__desc">seasoned with lemon juice, garlic, and olive oil</p></div>
  <div class="item" style="left:324px;top:484px"><div class="item__row"><span>White cheese</span><span class="item__price">L.E X.xx</span></div><p class="item__desc">with diced tomato, thyme, and olive oil</p></div>
  <div class="item" style="left:324px;top:512px"><div class="item__row"><span>Tehina</span><span class="item__price">L.E X.xx</span></div><p class="item__desc">seasoned with cumin, lemon juice, and garlic</p></div>

  <h2 class="section-head" style="left:324px;top:552px;width:250px">~Salads~</h2>
  <div class="item" style="left:324px;top:574px"><div class="item__row"><span>Caprese</span><span class="item__price">L.E X.xx</span></div><p class="item__desc" style="width:130px">Buffalo mozzarella and sliced tomato with a balsamic vinaigrette</p></div>
  <div class="item" style="left:324px;top:608px"><div class="item__row"><span>Rocket apple</span><span class="item__price">L.E X.xx</span></div><p class="item__desc" style="width:140px">Rocket leaves with gorgonzola, croutons, and strawberry vinaigrette</p></div>
  <div class="item" style="left:324px;top:642px"><div class="item__row"><span>French Riviera Nicoise</span><span class="item__price">L.E X.xx</span></div><p class="item__desc">Lettuce, egg, tomato, tuna, olives, onion, celery, radish, bell pepper in a French vinaigrette</p></div>
  <div class="item" style="left:324px;top:676px"><div class="item__row"><span>Folle</span><span class="item__price">L.E X.xx</span></div><p class="item__desc">Mixed greens with crab sticks, mushroom, corn, cherry tomato in a mango vinaigrette</p></div>
</section>

<div class="divider"></div>

<section class="page page--back">
  <div class="grass grass--top" style="left:210px;top:0;width:388px;height:30px" role="img" aria-label="green grass border"></div>
  <div class="grass grass--bottom" style="left:0;top:805px;width:598px;height:40px" role="img" aria-label="green grass border"></div>

  <h1 class="corner-title" style="left:0;top:35px;width:272px;text-align:center">Asian Corner</h1>
  <h1 class="corner-title" style="left:306px;top:35px;width:272px;text-align:center">Tex Mex</h1>

  <h2 class="section-head" style="left:26px;top:74px;width:250px">~Salads &amp; Appetizers~</h2>
  <div class="item" style="left:26px;top:96px"><div class="item__row"><span>Chicken wasabi salad</span><span class="item__price">L.E X.xx</span></div><p class="item__desc" style="width:150px">Diced chicken with a mayo wasabi dressing on top of shredded lettuce</p></div>
  <div class="item" style="left:26px;top:130px"><div class="item__row"><span>Chicken sesame noodle salad</span><span class="item__price">L.E X.xx</span></div><p class="item__desc" style="width:145px">Sesame crusted chicken with glass noodles tossed with sweet chili, soy sauce, and lemongrass</p></div>
  <div class="item" style="left:26px;top:164px"><div class="item__row"><span>Spring rolls</span><span class="item__price">L.E X.xx</span></div><p class="item__desc" style="width:150px">Vegetable spring rolls served with house made sweet and sour dip</p></div>
  <div class="item" style="left:26px;top:198px"><div class="item__row"><span>Indian samosa</span><span class="item__price">L.E X.xx</span></div><p class="item__desc">Fried dough parcels filled with vegetables and spices</p></div>

  <h2 class="section-head" style="left:26px;top:239px;width:250px">~Main Courses~</h2>
  <div class="item" style="left:26px;top:262px"><div class="item__row"><span>Murgh chicken makhni</span><span class="item__price">L.E X.xx</span></div><p class="item__desc" style="width:160px">Chicken cubes in a rich creamy tomato sauce seasoned with garam masala<br>Choice of side: vegetable korma or curd</p></div>
  <div class="item" style="left:26px;top:307px"><div class="item__row"><span>Chicken tandoori</span><span class="item__price">L.E X.xx</span></div><p class="item__desc" style="width:145px">Grilled chicken cubes with tandoori spices served with basmati rice</p></div>
  <div class="item" style="left:26px;top:345px"><div class="item__row"><span>Thai coconut curry shrimp</span><span class="item__price">L.E X.xx</span></div><p class="item__desc" style="width:150px">Sautéed shrimp tossed with curry and coconut milk served with jasmine rice</p></div>
  <div class="item" style="left:26px;top:383px"><div class="item__row"><span>Mongolian beef</span><span class="item__price">L.E X.xx</span></div><p class="item__desc" style="width:130px">Soy marinated beef with oyster sauce and vegetables served with egg noodles</p></div>

  <div class="photo" style="left:50px;top:452px;width:194px;height:166px;border-width:6px;background:linear-gradient(160deg,#e8e4de 0%,#5a3a22 55%,#d9b06a 100%)" role="img" aria-label="Photo of layered chocolate pastries on a platter"></div>

  <div class="brand-name" style="left:40px;top:712px">Lanterns</div>
  <div class="web" style="left:40px;top:752px">www.lanternsclubcairo.com</div>
  <p class="contact" style="left:51px;top:775px">Contact us: <em>Cairo, Egypt</em></p>
  <p class="contact" style="left:51px;top:804px">Tel: <em>(0321) 5550 1842</em></p>

  <h2 class="section-head" style="left:325px;top:74px;width:250px">~Salads &amp; Appetizers~</h2>
  <div class="item" style="left:325px;top:96px"><div class="item__row"><span>Caesar salad</span><span class="item__price">L.E X.xx</span></div><p class="item__desc" style="width:130px">Iceberg lettuce with Caesar dressing with grated Parmesan cheese and croutons</p></div>
  <div class="item" style="left:325px;top:131px"><div class="item__row"><span>Taco salad 42</span><span class="item__price">L.E X.xx</span></div><p class="item__desc" style="width:160px">Chicken breast, beans, sour cream, guacamole, tomato, corn, lettuce, olives, chives, vinaigrette</p></div>
  <div class="item" style="left:325px;top:165px"><div class="item__row"><span>Nachos</span><span class="item__price">L.E X.xx</span></div><p class="item__desc">topped with chili, melted cheese, beans</p></div>
  <div class="item" style="left:325px;top:192px"><div class="item__row"><span>Chicken Quesadilla</span><span class="item__price">L.E X.xx</span></div><p class="item__desc">served with guacamole, salsa, and sour cream</p></div>

  <h2 class="section-head" style="left:325px;top:234px;width:250px">~Main Courses &amp; Sandwiches~</h2>
  <div class="item" style="left:325px;top:257px"><div class="item__row"><span>Cheese burger</span><span class="item__price">L.E X.xx</span></div><p class="item__desc" style="width:130px">House made lean beef burger topped with cheddar cheese</p></div>
  <div class="item" style="left:325px;top:291px"><div class="item__row"><span>Mushroom burger</span><span class="item__price">L.E X.xx</span></div><p class="item__desc" style="width:140px">Beef burger with sautéed mushroom, caramelized onion, and provolone cheese</p></div>
  <div class="item" style="left:325px;top:325px"><div class="item__row"><span>Crispy chicken wrap</span><span class="item__price">L.E X.xx</span></div><p class="item__desc">Crisp fried chicken wrap with a ranch dressing</p></div>
  <div class="item" style="left:325px;top:352px"><div class="item__row"><span>Fajita (Chicken, Beef, Combo)</span><span class="item__price">L.E X.xx</span></div><p class="item__desc">pan seared meat or chicken with onion and bell pepper served with sour cream, guacamole, salsa</p></div>

  <h2 class="section-head" style="left:325px;top:398px;width:250px">~Desserts~</h2>
  <div class="item" style="left:325px;top:420px"><div class="item__row"><span>Mix berries cheesecake</span><span class="item__price">L.E X.xx</span></div></div>
  <div class="item" style="left:325px;top:441px"><div class="item__row"><span>Crème brulee</span><span class="item__price">L.E X.xx</span></div></div>
  <div class="item" style="left:325px;top:461px"><div class="item__row"><span>Chocolate caramel cake</span><span class="item__price">L.E X.xx</span></div></div>
  <div class="item" style="left:325px;top:482px"><div class="item__row"><span>Warm chocolate fondant</span><span class="item__price">L.E X.xx</span></div></div>
  <div class="item" style="left:325px;top:502px"><div class="item__row"><span>Baked apple tart tatin</span><span class="item__price">L.E X.xx</span></div></div>
  <div class="item" style="left:325px;top:523px"><div class="item__row"><span>Tiramisu</span><span class="item__price">L.E X.xx</span></div></div>
  <div class="item" style="left:325px;top:543px"><div class="item__row"><span>Pumpkin pie flan</span><span class="item__price">L.E X.xx</span></div></div>
  <div class="item" style="left:325px;top:564px"><div class="item__row"><span>Mixed berries granola yoghurt</span><span class="item__price">L.E X.xx</span></div></div>
  <div class="item" style="left:325px;top:584px"><div class="item__row"><span>Vanilla ice cream</span><span class="item__price">L.E X.xx</span></div><p class="item__desc">profiterole with dark and white chocolate sauce</p></div>
  <div class="item" style="left:325px;top:612px"><div class="item__row"><span>Caramelized banana</span><span class="item__price">L.E X.xx</span></div><p class="item__desc">with Deep Fried Ice Cream</p></div>
  <div class="item" style="left:325px;top:639px"><div class="item__row"><span>Baklava</span><span class="item__price">L.E X.xx</span></div><p class="item__desc">with Nuts and Sugar Syrup</p></div>
  <div class="item" style="left:325px;top:667px"><div class="item__row"><span>Shot glass sampler</span><span class="item__price">L.E X.xx</span></div><p class="item__desc">Tiramisu, Chocolate Crisp Mousse, Pear with Sabayon</p></div>
  <div class="item" style="left:325px;top:695px"><div class="item__row"><span>Ice cream</span><span class="item__price">L.E X.xx</span></div><p class="item__desc">by Scoop</p></div>
</section>

</div>
</body>
</html>
```